Wallaro Grove Premium Olive Oil Olive Oil 4 litre tin Lable

Hi designers, we need a label created for our South Australian Premium Olive oil 4 litre Tin. The Brand Is ( Wallaro Grove farms Premium Olive Oil) There must be a front and rear label.

The Front Label
Must have our Brand "Wallaro Grove Farms Premium Olive Oil "photo based scenic label highlighting the clean fresh and green environment this oil comes in Australia (Please see example of our location attached) can use generic pictures just see for inspiration, size must be 100mm wide 200mm height (see attached picture) It Must also indicate that its a 4 litre tin

The Rear Label
Same Size 100mm Wide x 200mm Height can be the same as the front expect allow space for nutritional information and add the address of our company. (Wallaro Grove Farms, Shopp4 218 Upper Kestrel Bend Road Marbury, South Australia 5182.

Hope you all have fun and happy designing.

Target Market(s)

High End Market

Font styles to use
Serif

Requirements
Must have
• Scenic Photo back ground (Clean and Green), show it is Australia.

```html
<!DOCTYPE html>
<html lang="en">
<head>
<meta charset="utf-8">
<title>Wallaro Grove Farms Premium Olive Oil – 4 Litre Tin Label</title>
<link rel="stylesheet" href="https://fonts.googleapis.com/css2?family=Cinzel:wght@400;500&family=EB+Garamond:wght@400&display=swap">
<style>
  :root {
    --page-bg: #ffffff;
    --green-deep: #0a260c;
    --green-mid: #1d5119;
    --green-bright: #3a8428;
    --gold: #d8ba68;
    --gold-light: #f3e09e;
    --gold-dark: #98762a;
    --sky-top: #6aaee4;
    --sky-low: #d9edf8;
    --hill-light: #a3c95c;
    --hill: #4f8f2b;
    --oil-shadow: #7c7f1c;
    --oil: #e6d043;
    --oil-deep: #b29a1d;
  }
  * { margin: 0; padding: 0; box-sizing: border-box; }
  html, body {
    width: 1200px; height: 943px; overflow: hidden;
    background: var(--page-bg);
  }
  .label {
    position: absolute; left: 390px; top: 51px;
    width: 420px; height: 840px;
    background: var(--green-deep);
    overflow: hidden;
    box-shadow: 0 2px 10px rgba(0,0,0,0.15);
  }
  .label__header {
    position: absolute; left: 0; top: 0; width: 100%; height: 462px;
    background: radial-gradient(ellipse 85% 70% at 50% 38%, var(--green-bright) 0%, var(--green-mid) 45%, var(--green-deep) 100%);
  }
  .crest {
    position: absolute; left: 70px; top: 36px; width: 280px; height: 180px;
  }
  .crest__frame { position: absolute; inset: 0; width: 100%; height: 100%; }
  .crest__name {
    position: absolute; left: 0; top: 62px; width: 100%;
    font-family: "EB Garamond", serif; font-size: 24px; line-height: 1.25;
    color: var(--gold); text-align: center;
  }
  .product-title {
    position: absolute; left: 0; top: 318px; width: 100%;
    text-align: center; color: var(--gold-light);
    font-family: "Cinzel", serif; font-weight: 500;
  }
  .product-title__premium { display: block; font-size: 40px; line-height: 1.1; letter-spacing: 1px; }
  .product-title__name { display: block; font-size: 62px; line-height: 1.05; letter-spacing: 1px; }
  .gold-rule {
    position: absolute; left: 0; top: 462px; width: 100%; height: 6px;
    background: linear-gradient(90deg, var(--gold-dark), var(--gold-light), var(--gold-dark));
  }
  .scenery {
    position: absolute; left: 0; top: 468px; width: 100%; height: 327px;
    background: linear-gradient(180deg,
      var(--sky-top) 0%, var(--sky-low) 16%,
      var(--hill-light) 26%, var(--hill) 36%,
      var(--oil-shadow) 48%, var(--oil) 68%,
      var(--oil) 82%, var(--oil-deep) 100%);
  }
  .label__footer {
    position: absolute; left: 0; top: 795px; width: 100%; height: 45px;
    border-top: 3px solid var(--gold-dark);
    background: var(--green-deep);
    display: flex; align-items: center; justify-content: center;
  }
  .volume {
    font-family: "Cinzel", serif; font-size: 11px; letter-spacing: 1px;
    color: var(--gold);
  }
</style>
</head>
<body>
  <main class="label">
    <section class="label__header">
      <div class="crest">
        <svg class="crest__frame" viewBox="0 0 280 180" aria-hidden="true">
          <ellipse cx="140" cy="90" rx="134" ry="84" fill="none" stroke="#d8ba68" stroke-width="2.5"/>
          <ellipse cx="140" cy="90" rx="124" ry="75" fill="none" stroke="#d8ba68" stroke-width="1"/>
        </svg>
        <p class="crest__name">Wallaro Grove<br>Farms</p>
      </div>
      <h1 class="product-title">
        <span class="product-title__premium">Premium</span>
        <span class="product-title__name">Olive Oil</span>
      </h1>
    </section>
    <div class="gold-rule"></div>
    <div class="scenery" role="img" aria-label="Green rolling South Australian hills under a blue sky, with dark olives resting in golden olive oil"></div>
    <footer class="label__footer">
      <span class="volume">4 LITRE TIN</span>
    </footer>
  </main>
</body>
</html>
```